The amber lantern with an elephant incorporated in the background

Target Market(s)

Real estate

Industry/Entity Type

Real Estate

Contact Information for Business Card

On back on want my name & number
In front I want the business name, "the amber lantern", below to say staging & design

Logo Text

The amber lantern

Font styles to use
Serif

Colors
000000

Requirements
Must have
• I want an elephant behind the writing in gold transperant

```html
<!DOCTYPE html>
<html lang="en">
<head>
<meta charset="utf-8">
<title>The Amber Lantern — Business Card</title>
<link rel="stylesheet" href="https://fonts.googleapis.com/css2?family=Josefin+Sans:wght@300;400&family=Dancing+Script:wght@400&display=swap">
<style>
  :root {
    --stage: #e9e6e1;
    --card-black: #060606;
    --gloss: #3a3a3a;
    --ink-white: #f4f4f2;
    --accent-yellow: #cbbf35;
    --accent-yellow-deep: #9c9120;
    --elephant-gold: rgba(176, 150, 40, 0.28);
  }
  * { margin: 0; padding: 0; box-sizing: border-box; }
  html, body {
    width: 1200px; height: 804px; overflow: hidden;
    background: var(--stage);
  }
  .stage {
    position: relative; width: 1200px; height: 804px;
  }
  .card {
    position: absolute; top: 259px;
    width: 500px; height: 286px;
    border-radius: 16px;
    background: var(--card-black);
    overflow: hidden;
    box-shadow: 0 6px 18px rgba(0,0,0,0.18);
    color: var(--ink-white);
    font-family: "Josefin Sans", sans-serif;
    font-weight: 300;
  }
  .card--front { left: 70px; }
  .card--back { left: 630px; }
  .card__gloss {
    position: absolute; left: -60px; bottom: -110px;
    width: 300px; height: 200px;
    background: radial-gradient(ellipse at center, var(--gloss) 0%, rgba(58,58,58,0.5) 40%, rgba(6,6,6,0) 72%);
  }

  /* Front */
  .brand-mark {
    position: absolute; left: 185px; top: 40px;
    width: 170px; height: 170px; border-radius: 50%;
    background: var(--elephant-gold);
  }
  .brand-name {
    position: absolute; left: 0; right: 0; top: 118px;
    text-align: center;
    font-size: 31px; letter-spacing: 1.5px;
    text-transform: uppercase;
  }
  .brand-tagline {
    position: absolute; left: 210px; top: 160px;
    font-family: "Dancing Script", cursive;
    font-size: 17px; letter-spacing: 1px;
  }

  /* Back */
  .person {
    position: absolute; right: 48px; top: 44px;
    text-align: center;
  }
  .person__name { font-size: 24px; letter-spacing: 1px; }
  .person__role { font-size: 12px; margin-top: 6px; }

  .contact-tab {
    position: absolute; left: 0; top: 136px;
    width: 84px; height: 24px;
    background: var(--accent-yellow);
    border-radius: 0 5px 5px 0;
  }
  .contact-icon {
    position: absolute; left: 62px;
    width: 22px; height: 22px; border-radius: 4px;
    background: var(--accent-yellow);
    display: flex; align-items: center; justify-content: center;
  }
  .contact-icon svg { width: 13px; height: 13px; fill: var(--card-black); }
  .contact-icon--pin { top: 137px; background: none; }
  .contact-icon--phone { top: 166px; }
  .contact-icon--mail { top: 194px; }
  .contact-list {
    position: absolute; left: 100px; top: 140px;
    list-style: none;
  }
  .contact-list li { line-height: 28px; }
  .contact-list .phone { font-size: 17px; letter-spacing: 1px; }
  .contact-list .email { font-size: 12px; }

  .skyline {
    position: absolute; left: 150px; right: 0; bottom: 0;
    height: 150px;
    background: linear-gradient(to top, var(--accent-yellow-deep) 0%, var(--accent-yellow) 35%, rgba(203,191,53,0) 100%);
    clip-path: polygon(0 100%, 0 85%, 30% 70%, 55% 40%, 80% 10%, 100% 0, 100% 100%);
    opacity: 0.9;
  }
</style>
</head>
<body>
<main class="stage">
  <section class="card card--front" aria-label="Business card front">
    <div class="card__gloss"></div>
    <div class="brand-mark" role="img" aria-label="Transparent gold elephant behind the business name"></div>
    <h1 class="brand-name">The Amber Lantern</h1>
    <p class="brand-tagline">staging &amp; design</p>
  </section>

  <section class="card card--back" aria-label="Business card back">
    <div class="card__gloss"></div>
    <div class="skyline" role="img" aria-label="Sketched yellow city skyline along the bottom edge"></div>
    <div class="person">
      <h2 class="person__name">YOUR NAME</h2>
      <p class="person__role">Designation</p>
    </div>
    <div class="contact-tab"></div>
    <span class="contact-icon contact-icon--pin">
      <svg viewBox="0 0 24 24" aria-hidden="true"><path d="M12 2a7 7 0 0 0-7 7c0 5 7 13 7 13s7-8 7-13a7 7 0 0 0-7-7zm0 9.5A2.5 2.5 0 1 1 12 6.5a2.5 2.5 0 0 1 0 5z"/></svg>
    </span>
    <span class="contact-icon contact-icon--phone">
      <svg viewBox="0 0 24 24" aria-hidden="true"><path d="M6.6 10.8a15 15 0 0 0 6.6 6.6l2.2-2.2a1 1 0 0 1 1-.25 11.4 11.4 0 0 0 3.6.57 1 1 0 0 1 1 1V20a1 1 0 0 1-1 1A17 17 0 0 1 3 4a1 1 0 0 1 1-1h3.5a1 1 0 0 1 1 1c0 1.25.2 2.45.57 3.6a1 1 0 0 1-.25 1z"/></svg>
    </span>
    <span class="contact-icon contact-icon--mail">
      <svg viewBox="0 0 24 24" aria-hidden="true"><path d="M3 5h18v14H3zm2 2v.4l7 4.6 7-4.6V7zm0 2.8V17h14V9.8l-7 4.6z"/></svg>
    </span>
    <ul class="contact-list">
      <li class="phone">01632 960481</li>
      <li class="email">theamberlantern@mailbox.com</li>
    </ul>
  </section>
</main>
</body>
</html>
```